Halvern Dental website redesign

We need a redesign for a website: myhalverndental.com.

I already created a video going over what exactly is needed in the design.

See Video here: https://files.quorvane.com/file/d/8xKpQ2mWn4TzLrV7bHsYcE3jFuGaD6oN1/view?usp=sharing

Google Slide shown in Video: https://slides.quorvane.com/presentation/d/7RtW2yQnXbVc4LmPz9KsHdJf3GaE8oUi6TeYqNvB5wZx/edit?usp=sharing
Updates

Holidays in India so we did not get enough design entries or quality.

Target Market(s)

Dentistry

Industry/Entity Type

Dentistry

Number of Pages Required

1 page

Colors
0094D4
00A9DD
6FCCEA
C7EBF8
E9F6FB
00AB8E
00BBA5
67D7C9
C6EFE9
E9F9F6

Requirements
Must have
• See 13 min video link in description - shows what to do.

```html
<!DOCTYPE html>
<html lang="en">
<head>
<meta charset="utf-8">
<title>Halvern Dental</title>
<link href="https://fonts.googleapis.com/css2?family=Roboto:wght@400;500;700;900&display=swap" rel="stylesheet">
<style>
:root{
  --blue:#0094D4;
  --blue-mid:#00A9DD;
  --blue-dark:#007bb0;
  --teal:#00AB8E;
  --teal-mid:#00BBA5;
  --teal-dark:#008f77;
  --pale-blue:#E9F6FB;
  --light-blue:#C7EBF8;
  --text:#555;
  --title:#333;
  --muted:#aaa;
  --star:#f6b400;
  --footer:#1f1f1f;
  --white:#fff;
}
*{box-sizing:border-box;margin:0;padding:0}
html,body{width:1200px;height:3133px;overflow:hidden;background:var(--white);font-family:'Roboto',sans-serif;color:var(--text)}
.page{position:relative;width:1200px;height:3133px}
.wrap{width:750px;margin:0 auto;position:relative}
a{color:inherit;text-decoration:none}
.btn{display:inline-flex;align-items:center;justify-content:center;background:var(--blue);color:var(--white);font-weight:700;font-size:10px;border-radius:14px}
.btn.teal{background:var(--teal)}

/* top bar */
.topbar{height:25px;background:var(--blue);color:var(--white);font-size:11px}
.topbar .wrap{display:flex;justify-content:space-between;align-items:center;height:25px}
.topbar .phone{display:flex;align-items:center;gap:8px}
.topbar .follow{display:flex;align-items:center;gap:8px}
.dot{width:15px;height:15px;border-radius:50%;background:var(--white);display:inline-block}

/* header */
.header{height:80px;background:var(--white);box-shadow:0 3px 8px rgba(0,0,0,.05);position:relative;z-index:2}
.brand{position:absolute;left:2px;top:20px;display:flex;align-items:center;gap:8px;font-size:20px;font-weight:500;color:var(--blue)}
.brand .mark{width:14px;height:14px;border-radius:50%;background:var(--teal)}
.header .cta{position:absolute;right:0;top:13px;display:flex;gap:8px}
.header .cta .btn{height:25px;border-radius:13px}
.header .cta .schedule{width:110px}
.header .cta .emergency{width:87px}
.nav{position:absolute;right:0;top:53px;display:flex;gap:19px;font-size:12px;color:#444}
.nav span.caret::after{content:"";display:inline-block;width:5px;height:5px;border-right:1.3px solid #444;border-bottom:1.3px solid #444;transform:rotate(45deg);margin-left:7px;position:relative;top:-2px}

/* hero */
.hero{height:342px;position:relative}
.hero h1{position:absolute;left:0;top:118px;font-size:35px;font-weight:900;color:var(--blue);letter-spacing:-.2px}
.hero p{position:absolute;left:0;top:165px;font-size:13px;color:#444}
.hero .btn{position:absolute;left:0;top:199px;width:135px;height:26px}
.hero .photo{position:absolute;left:492px;top:12px;width:231px;height:330px;background:linear-gradient(180deg,#eef7fb,#d6ecf5);border-radius:110px 110px 0 0}

/* team */
.team{height:463px;background:var(--pale-blue)}
.section-title{text-align:center;font-size:19px;font-weight:700;color:var(--title);line-height:23px}
.team .section-title{padding-top:34px}
.team-grid{display:flex;justify-content:space-between;margin-top:34px}
.doc{width:213px;height:344px;background:var(--white);position:relative}
.doc .portrait{height:175px;background:linear-gradient(160deg,#6c7c88,#3a4650)}
.doc h3{font-size:12px;font-weight:700;color:var(--title);margin:14px 18px 10px}
.doc p{font-size:11px;line-height:19.5px;margin:0 18px;color:var(--text)}
.doc .more{position:absolute;left:18px;right:18px;bottom:12px;display:flex;gap:18px;align-items:center;font-size:11px;color:var(--blue-dark)}
.arrow{width:13px;height:13px;border-radius:50%;background:var(--blue-dark);display:inline-flex;align-items:center;justify-content:center}

/* services */
.services{height:354px}
.services .section-title{padding-top:32px;color:var(--blue-dark)}
.svc-grid{display:grid;grid-template-columns:repeat(4,173px);column-gap:19px;row-gap:17px;margin-top:26px}
.svc{height:57px;background:var(--white);box-shadow:0 2px 10px rgba(0,0,0,.08);display:flex;align-items:center;gap:10px;padding-left:12px;font-size:12px;font-weight:700;color:var(--blue)}
.svc svg{width:22px;height:22px;flex:none}

/* reviews */
.reviews{height:724px}
.reviews .section-title{padding-top:0;color:#222}
.rev-grid{display:grid;grid-template-columns:repeat(3,225px);column-gap:37px;row-gap:25px;margin-top:30px}
.rev{height:292px;background:var(--white);box-shadow:0 2px 12px rgba(0,0,0,.08);position:relative}
.rev .avatar{position:absolute;left:19px;top:20px;width:62px;height:62px;border-radius:50%;background:#ececec;overflow:hidden}
.rev .avatar::before{content:"";position:absolute;left:20px;top:12px;width:22px;height:22px;border-radius:50%;background:#c9c9c9}
.rev .avatar::after{content:"";position:absolute;left:11px;top:38px;width:40px;height:30px;border-radius:20px 20px 0 0;background:#c9c9c9}
.rev .stars{position:absolute;left:94px;top:14px;display:flex;gap:5px}
.rev .name{position:absolute;left:94px;top:59px;font-size:14px;font-weight:700;color:#333}
.rev .body{position:absolute;left:19px;right:17px;top:100px;font-size:9px;line-height:14.5px;color:#555}
.rev .body em{font-style:normal;color:var(--teal)}
.rev .date{position:absolute;left:19px;top:200px;font-size:11px;color:var(--muted)}
.rev .foot{position:absolute;left:0;right:0;top:223px;border-top:1px solid #ececec;height:69px;display:flex;align-items:center;justify-content:space-between;padding:0 19px;font-size:10px;color:#333}
.rev .source-name{font-size:17px;font-weight:700;color:#222;display:flex;align-items:center;gap:4px}
.rev .source-name i{width:9px;height:9px;border-radius:50%;background:#e02020;display:inline-block}

/* difference */
.difference{height:672px}
.difference .section-title{padding-top:0;color:var(--blue-dark)}
.diff-grid{display:grid;grid-template-columns:repeat(3,225px);column-gap:37px;row-gap:32px;margin-top:33px}
.diff{height:260px;background:var(--white);box-shadow:0 2px 12px rgba(0,0,0,.07);text-align:center;padding:28px 18px 0}
.diff .icon{height:48px;display:flex;align-items:center;justify-content:center;color:var(--teal)}
.diff .num{font-size:44px;font-weight:900;color:var(--teal);letter-spacing:1px}
.diff p{margin-top:22px;font-size:11px;line-height:19.5px;color:var(--text)}

/* cta band */
.band{height:228px;position:relative;text-align:center;color:var(--white);background:linear-gradient(90deg,#0078ad 0%,#0094D4 50%,#00967d 100%)}
.band h2{padding-top:41px;font-size:18px;font-weight:700}
.band p{margin-top:11px;font-size:12px}
.band .icons{display:flex;justify-content:center;gap:28px;margin-top:14px}
.band .btn{margin-top:13px;width:134px;height:24px}

/* footer */
.footer{height:245px;background:var(--footer);color:var(--white);position:relative;font-size:10px}
.fcol{position:absolute;top:32px}
.fcol h4{font-size:10px;font-weight:500;margin-bottom:12px;text-transform:uppercase}
.fcol p{line-height:22px}
.fcol .link{color:var(--blue-mid)}
.fcol .social{display:flex;gap:10px}
.fcol .social .dot{width:16px;height:16px}
.map{width:155px;height:124px;background:linear-gradient(135deg,#eef3f6,#dbe5ec);border-radius:2px;margin-top:-2px}
.footer .btn{width:83px;height:25px;font-size:10px}
.footer .rule{position:absolute;left:225px;right:225px;top:207px;border-top:1px solid #3a3a3a}
.footer .copy{position:absolute;left:0;right:0;top:220px;text-align:center;font-size:9px}
</style>
</head>
<body>
<div class="page">

  <div class="topbar">
    <div class="wrap">
      <div class="phone">
        <svg width="14" height="14" viewBox="0 0 24 24"><circle cx="12" cy="12" r="12" fill="#fff"/><path d="M8.2 6.5l2 2.3-1.2 1.4c.8 1.8 2.2 3.2 4 4l1.4-1.2 2.3 2-1 1.7c-4.5-.3-8.3-4.1-8.6-8.6z" fill="#0094D4"/></svg>
        <span>(555) 302-4187</span>
      </div>
      <div class="follow">
        <span>Follow Us</span>
        <span class="dot"></span><span class="dot"></span><span class="dot"></span><span class="dot"></span>
      </div>
    </div>
  </div>

  <header class="header">
    <div class="wrap" style="height:80px">
      <div class="brand"><span>Halvern Dental</span><span class="mark"></span></div>
      <div class="cta">
        <a class="btn schedule">Schedule Online</a>
        <a class="btn teal emergency">Emergency</a>
      </div>
      <nav class="nav">
        <span>About Us</span><span class="caret">Services</span><span>Financing</span><span>Testimonials</span><span>New Patient Visit</span><span>Specials</span><span>Contact Us</span><span>Blog</span>
      </nav>
    </div>
  </header>

  <section class="hero">
    <div class="wrap" style="height:342px">
      <h1>Creating Healthier Smiles</h1>
      <p>With Advanced Technology and Affordable Treatment</p>
      <a class="btn">Book an Appointment</a>
      <div class="photo" role="img" aria-label="Smiling woman holding a dental model and toothbrush"></div>
    </div>
  </section>

  <section class="team">
    <h2 class="section-title">Our Team</h2>
    <div class="wrap team-grid">
      <article class="doc">
        <div class="portrait" role="img" aria-label="Portrait of Dr. Ravin Mehra"></div>
        <h3>Dr. Ravin Mehra</h3>
        <p>DDS has been dedicated to providing quality dental care to his patients for 20+ years</p>
        <a class="more">Meet Dr. Ravin Mehra <span class="arrow"><svg width="7" height="7" viewBox="0 0 10 10"><path d="M1 5h7M5 2l3 3-3 3" stroke="#fff" stroke-width="1.6" fill="none"/></svg></span></a>
      </article>
      <article class="doc">
        <div class="portrait" role="img" aria-label="Portrait of Dr. Anjali Desai" style="background:linear-gradient(160deg,#5a6f86,#2c3a4a)"></div>
        <h3>Dr. Anjali Desai</h3>
        <p>DDS graduated from Westmont University, Harold K. Lane School of Dentistry and is a member of several professional organizations.</p>
        <a class="more">Meet Dr. Anjali Desai <span class="arrow"><svg width="7" height="7" viewBox="0 0 10 10"><path d="M1 5h7M5 2l3 3-3 3" stroke="#fff" stroke-width="1.6" fill="none"/></svg></span></a>
      </article>
      <article class="doc">
        <div class="portrait" role="img" aria-label="Portrait of Dr. Priya Nanda"></div>
        <h3>Dr. Priya Nanda</h3>
        <p>DDS is inspired by making an impact on the lives of others by alleviating their pain and returning their smiles.</p>
        <a class="more">Meet Dr. Priya Nanda <span class="arrow"><svg width="7" height="7" viewBox="0 0 10 10"><path d="M1 5h7M5 2l3 3-3 3" stroke="#fff" stroke-width="1.6" fill="none"/></svg></span></a>
      </article>
    </div>
  </section>

  <section class="services">
    <h2 class="section-title">Services</h2>
    <div class="wrap svc-grid">
      <div class="svc"><svg viewBox="0 0 24 24"><path d="M6 3c2 0 3 1 6 1s4-1 6-1c2 0 3 2 3 5 0 4-2 6-3 11-.3 2-2 2-2.3 0L14.5 14c-.5-2-4.5-2-5 0L8.3 19c-.3 2-2 2-2.3 0C5 14 3 12 3 8c0-3 1-5 3-5z" fill="#00AB8E"/></svg>Dental Implants</div>
      <div class="svc"><svg viewBox="0 0 24 24"><path d="M3 8h18M5 8c0 6 3 10 7 10s7-4 7-10" stroke="#00AB8E" stroke-width="2" fill="none"/><circle cx="12" cy="5" r="2" fill="#00AB8E"/></svg>Cosmetic Dentistry</div>
      <div class="svc"><svg viewBox="0 0 24 24"><path d="M6 3c2 0 3 1 6 1s4-1 6-1c2 0 3 2 3 5 0 4-2 6-3 11-.3 2-2 2-2.3 0L14.5 14c-.5-2-4.5-2-5 0L8.3 19c-.3 2-2 2-2.3 0C5 14 3 12 3 8c0-3 1-5 3-5z" fill="#00AB8E"/><path d="M3 9h18" stroke="#fff" stroke-width="1.5"/></svg>Braces</div>
      <div class="svc"><svg viewBox="0 0 24 24"><path d="M3 6l4 3 5-5 5 5 4-3v9H3z" fill="#00AB8E"/><rect x="3" y="16" width="18" height="3" fill="#00AB8E"/></svg>Crowns</div>
      <div class="svc"><svg viewBox="0 0 24 24"><rect x="2" y="6" width="6" height="10" rx="2" fill="#00AB8E"/><rect x="9" y="6" width="6" height="10" rx="2" fill="#00AB8E"/><rect x="16" y="6" width="6" height="10" rx="2" fill="#00AB8E"/><path d="M2 11h20" stroke="#fff" stroke-width="1.5"/></svg>Bridge</div>
      <div class="svc"><svg viewBox="0 0 24 24"><path d="M7 9c1 0 2 1 5 1s4-1 5-1c1 0 2 1 2 3 0 3-2 4-2 8h-2l-1-4h-4l-1 4H7c0-4-2-5-2-8 0-2 1-3 2-3z" fill="#00AB8E"/><path d="M12 2v5M9 5l3 3 3-3" stroke="#00AB8E" stroke-width="1.6" fill="none"/></svg>Extractions</div>
      <div class="svc"><svg viewBox="0 0 24 24"><path d="M3 14c3-3 15-3 18 0v6H3z" fill="#00AB8E"/><rect x="5" y="6" width="4" height="7" rx="1.5" fill="#00AB8E"/><rect x="10" y="5" width="4" height="8" rx="1.5" fill="#00AB8E"/><rect x="15" y="6" width="4" height="7" rx="1.5" fill="#00AB8E"/></svg>Gum Disease</div>
      <div class="svc"><svg viewBox="0 0 24 24"><path d="M6 3c2 0 3 1 6 1s4-1 6-1c2 0 3 2 3 5 0 4-2 6-3 11-.3 2-2 2-2.3 0L14.5 14c-.5-2-4.5-2-5 0L8.3 19c-.3 2-2 2-2.3 0C5 14 3 12 3 8c0-3 1-5 3-5z" fill="none" stroke="#00AB8E" stroke-width="2"/><path d="M10 8v8M14 8v8" stroke="#00AB8E" stroke-width="1.5"/></svg>Root Canal</div>
      <div class="svc"><svg viewBox="0 0 24 24"><rect x="2" y="6" width="20" height="12" rx="5" fill="#00AB8E"/><path d="M7 6v12M12 6v12M17 6v12M2 12h20" stroke="#fff" stroke-width="1.3"/></svg>Dentures</div>
      <div class="svc"><svg viewBox="0 0 24 24"><path d="M7 20v-7a5 5 0 0 1 10 0v7z" fill="#00AB8E"/><rect x="5" y="19" width="14" height="2" fill="#00AB8E"/><path d="M12 2v3M4 6l2 2M20 6l-2 2" stroke="#00AB8E" stroke-width="1.6"/></svg>Emergency Dentistry</div>
      <div class="svc"><svg viewBox="0 0 24 24"><path d="M2 8c4-2 16-2 20 0l-2 4H4z" fill="#00AB8E"/><rect x="5" y="12" width="3" height="6" rx="1" fill="#00AB8E"/><rect x="10.5" y="12" width="3" height="7" rx="1" fill="#00AB8E"/><rect x="16" y="12" width="3" height="6" rx="1" fill="#00AB8E"/></svg>Veneers</div>
      <div class="svc"><svg viewBox="0 0 24 24"><path d="M2 5h20M2 19h20" stroke="#00AB8E" stroke-width="1.5" stroke-dasharray="2 1.5"/><rect x="3" y="8" width="18" height="8" rx="3" fill="#00AB8E"/><path d="M7 8v8M12 8v8M17 8v8" stroke="#fff" stroke-width="1.2"/></svg>ClearFit Aligners</div>
    </div>
  </section>

  <section class="reviews">
    <h2 class="section-title">What Our Patients Say About Us</h2>
    <div class="wrap rev-grid">
      <article class="rev">
        <div class="avatar"></div>
        <div class="stars"><svg width="110" height="17" viewBox="0 0 110 17"><g fill="#f6b400"><path id="s" d="M8.5 0l2.6 5.5 6 .6-4.5 4 1.3 6-5.4-3.1L3.1 16l1.3-6L0 6.1l6-.6z"/><use href="#s" x="22"/><use href="#s" x="44"/><use href="#s" x="66"/><use href="#s" x="88"/></g></svg></div>
        <div class="name">Marisol T.</div>
        <p class="body">I just would like to talk about my experience at Halvern Dental ! It was my first time going there to get some dental work done ! 4 crowns and a extraction ! And let me say the whole entire staff was very professional ,... <em>more</em></p>
        <div class="date">20 October, 2021</div>
        <div class="foot"><span>Source:</span><span class="source-name">Revuo<i></i></span></div>
      </article>
      <article class="rev">
        <div class="avatar"></div>
        <div class="stars"><svg width="110" height="17" viewBox="0 0 110 17"><g fill="#f6b400"><use href="#s"/><use href="#s" x="22"/><use href="#s" x="44"/><use href="#s" x="66"/><use href="#s" x="88"/></g></svg></div>
        <div class="name">Marisol T.</div>
        <p class="body">I just would like to talk about my experience at Halvern Dental ! It was my first time going there to get some dental work done ! 4 crowns and a extraction ! And let me say the whole entire staff was very professional ,... <em>more</em></p>
        <div class="date">20 October, 2021</div>
        <div class="foot"><span>Source:</span><span class="source-name">Revuo<i></i></span></div>
      </article>
      <article class="rev">
        <div class="avatar"></div>
        <div class="stars"><svg width="110" height="17" viewBox="0 0 110 17"><g fill="#f6b400"><use href="#s"/><use href="#s" x="22"/><use href="#s" x="44"/><use href="#s" x="66"/><use href="#s" x="88"/></g></svg></div>
        <div class="name">Marisol T.</div>
        <p class="body">I just would like to talk about my experience at Halvern Dental ! It was my first time going there to get some dental work done ! 4 crowns and a extraction ! And let me say the whole entire staff was very professional ,... <em>more</em></p>
        <div class="date">20 October, 2021</div>
        <div class="foot"><span>Source:</span><span class="source-name">Revuo<i></i></span></div>
      </article>
      <article class="rev">
        <div class="avatar"></div>
        <div class="stars"><svg width="110" height="17" viewBox="0 0 110 17"><g fill="#f6b400"><use href="#s"/><use href="#s" x="22"/><use href="#s" x="44"/><use href="#s" x="66"/><use href="#s" x="88"/></g></svg></div>
        <div class="name">Marisol T.</div>
        <p class="body">I just would like to talk about my experience at Halvern Dental ! It was my first time going there to get some dental work done ! 4 crowns and a extraction ! And let me say the whole entire staff was very professional ,... <em>more</em></p>
        <div class="date">20 October, 2021</div>
        <div class="foot"><span>Source:</span><span class="source-name">Revuo<i></i></span></div>
      </article>
      <article class="rev">
        <div class="avatar"></div>
        <div class="stars"><svg width="110" height="17" viewBox="0 0 110 17"><g fill="#f6b400"><use href="#s"/><use href="#s" x="22"/><use href="#s" x="44"/><use href="#s" x="66"/><use href="#s" x="88"/></g></svg></div>
        <div class="name">Marisol T.</div>
        <p class="body">I just would like to talk about my experience at Halvern Dental ! It was my first time going there to get some dental work done ! 4 crowns and a extraction ! And let me say the whole entire staff was very professional ,... <em>more</em></p>
        <div class="date">20 October, 2021</div>
        <div class="foot"><span>Source:</span><span class="source-name">Revuo<i></i></span></div>
      </article>
      <article class="rev">
        <div class="avatar"></div>
        <div class="stars"><svg width="110" height="17" viewBox="0 0 110 17"><g fill="#f6b400"><use href="#s"/><use href="#s" x="22"/><use href="#s" x="44"/><use href="#s" x="66"/><use href="#s" x="88"/></g></svg></div>
        <div class="name">Marisol T.</div>
        <p class="body">I just would like to talk about my experience at Halvern Dental ! It was my first time going there to get some dental work done ! 4 crowns and a extraction ! And let me say the whole entire staff was very professional ,... <em>more</em></p>
        <div class="date">20 October, 2021</div>
        <div class="foot"><span>Source:</span><span class="source-name">Revuo<i></i></span></div>
      </article>
    </div>
  </section>

  <section class="difference">
    <h2 class="section-title">Experience the Halvern Dental Difference</h2>
    <div class="wrap diff-grid">
      <div class="diff">
        <div class="icon"><span class="num">#1</span></div>
        <p>Your smile is our #1 priority. At Halvern Dental, we provide affordable and expert dental solutions. Wether you are looking for a family dentist or have any emergency</p>
      </div>
      <div class="diff">
        <div class="icon"><svg width="36" height="40" viewBox="0 0 24 26"><path d="M6 1c2 0 3 1 6 1s4-1 6-1c3 0 5 2.5 5 6.5 0 5-3 8-4 15-.4 3-2.6 3-3 0l-1.3-6c-.5-2-4.9-2-5.4 0L8 22.5c-.4 3-2.6 3-3 0C4 15.5 1 12.5 1 7.5 1 3.5 3 1 6 1z" fill="#00AB8E"/></svg></div>
        <p>We are here for you! We want to keep your teeth healthy inside and out. We don't just clean teeth and send you on your way, we want to get to know you.</p>
      </div>
      <div class="diff">
        <div class="icon"><svg width="34" height="40" viewBox="0 0 24 28"><path d="M12 1l10 4v8c0 7-4.5 11.5-10 14C6.5 24.5 2 20 2 13V5z" fill="#00AB8E"/><path d="M12 8v10M7 13h10" stroke="#fff" stroke-width="3"/></svg></div>
        <p>We accept most HMO and PPO insurances. We offer various financing options through CarePlus Finance, LendWell and In-House Plans.</p>
      </div>
      <div class="diff">
        <div class="icon"><svg width="38" height="40" viewBox="0 0 30 32"><circle cx="21" cy="4" r="3" fill="#00AB8E"/><path d="M19 8h5v10h-3v12h-3V18" fill="#00AB8E"/><path d="M2 10l4 10h10l2 4v6M8 20l-2 10M2 8h5" stroke="#00AB8E" stroke-width="2.4" fill="none"/><rect x="6" y="12" width="9" height="3" fill="#00AB8E"/></svg></div>
        <p>To constantly strive to achieve the highest level of skills and modern techniques and equipment so we can provide our patients with the best that Dentistry has to offer at our dental office in Brookfield, Lakeview County, CA.</p>
      </div>
      <div class="diff">
        <div class="icon"><svg width="50" height="38" viewBox="0 0 40 30"><circle cx="13" cy="7" r="6" fill="#00AB8E"/><circle cx="28" cy="7" r="6" fill="#00AB8E"/><path d="M1 29c0-8 5-13 12-13s12 5 12 13z" fill="#00AB8E"/><path d="M27 29c0-6-1-9-4-12 2-1 3-1 5-1 7 0 11 5 11 13z" fill="#00AB8E"/></svg></div>
        <p>We provide patients with the best experience you can find in all of Northern Valley. We provide a comfortable and friendly atmosphere to shatter any fears you may have.</p>
      </div>
      <div class="diff">
        <div class="icon"><svg width="30" height="40" viewBox="0 0 22 28"><path d="M0 2a2 2 0 0 1 2-2h12l8 8v18a2 2 0 0 1-2 2H2a2 2 0 0 1-2-2z" fill="#00AB8E"/><path d="M14 0v8h8" fill="#008f77"/><path d="M8 14h9M8 18h9M8 22h9" stroke="#fff" stroke-width="1.6"/><circle cx="5" cy="14" r="1" fill="#fff"/><circle cx="5" cy="18" r="1" fill="#fff"/><circle cx="5" cy="22" r="1" fill="#fff"/></svg></div>
        <p>We supply you with all the information on your dental health options so you can feel comfortable in the choices you make, whether it's a routine check-up or dental implants in Brookfield.</p>
      </div>
    </div>
  </section>

  <section class="band" role="img" aria-label="Patient in a dental chair under a blue tint">
    <h2>Committed to excellence in Oral Health Care</h2>
    <p>Free Exam and X-Rays for New Patients</p>
    <div class="icons">
      <svg width="40" height="40" viewBox="0 0 40 40" fill="none" stroke="#fff" stroke-width="2"><rect x="4" y="6" width="24" height="30" rx="2"/><rect x="11" y="3" width="10" height="6" rx="1"/><path d="M9 16h14M9 22h14M9 28h10"/><path d="M33 8v26l-2 3-2-3V8z"/></svg>
      <svg width="40" height="40" viewBox="0 0 40 40" fill="none" stroke="#fff" stroke-width="2"><rect x="4" y="4" width="32" height="32" rx="3"/><path d="M14 10c2 0 3 1 6 1s4-1 6-1c2 0 3 2 3 4 0 4-2 5-3 11-.3 2-2 2-2.3 0L22 20c-.5-1-3.5-1-4 0l-1.7 6c-.3 2-2 2-2.3 0-1-6-3-7-3-11 0-2 1-4 3-4z"/><path d="M14 16h12"/></svg>
    </div>
    <a class="btn teal">Book an Appointment</a>
  </section>

  <footer class="footer">
    <div class="fcol" style="left:241px">
      <h4>Halvern Dental</h4>
      <p>482 North Ellison Ave., Suite B<br>Brookfield, CA 94015</p>
      <h4 style="margin-top:14px">Contact Us</h4>
      <p class="link">(555)302 4187<br>halverndental@mailnest.com</p>
    </div>
    <div class="fcol" style="left:428px">
      <h4>Office Hours</h4>
      <p>Monday 10AM–7PM<br>Tuesday 10AM–7PM<br>Wednesday 9AM–6PM<br>Thursday 9AM–6PM<br>Friday 9AM–5PM<br>Saturday 9AM–1PM</p>
    </div>
    <div class="fcol" style="left:617px">
      <h4>Maps &amp; Directions</h4>
      <div class="map" role="img" aria-label="Street map showing the office location"></div>
    </div>
    <div class="fcol" style="left:818px">
      <h4>Follow Us</h4>
      <div class="social"><span class="dot"></span><span class="dot"></span><span class="dot"></span><span class="dot"></span></div>
      <h4 style="margin-top:18px">Book Your Appointment</h4>
      <a class="btn">Book Now</a>
    </div>
    <div class="rule"></div>
    <div class="copy">© All Rigths Reserved</div>
  </footer>

</div>
</body>
</html>
```